Product Label

We need a label to go with our logo. This label will go on all of our packaging. It needs to be able to be modified for each product that we sell. That means one label will be for Broccoli Microgreens, one for Sunflower Microgreens, one for Radish Microgreens, etc. At the current time we have approximately 20 different products that would go with this label. That is one product per label for 20 + labels. We are asking for one
design that is easily changed for each product.

The colors should work with the colors in our logo for an appealing overall look and brand.

The label should be 4 inches x 4 inches or 3 inches x 4 inches. We are not sure which will look the best.

The following should be on the label:

Our logo. It is uploaded please let me know if you need other formats. It was created here at Pixel Harbor.

Product name, for example Sunflower Microgreens. This should stand out and be easily changed.

The following is our tag line
Naturally Grown Immune Boosting Antioxidant Supperfood

The following can be in the form of bullets and arranged together. There is no special order on them. What ever is a good visual works. We are thinking the leaves in the upper part of logo may work for the bullet points.

Locally Grown
Non GMO
Grown With Organic Seeds

The following items should be set aside from the other bullets.
Net WT. 2 OZ
Keep Refrigerated
Thoroughly Wash Before Use

We would like to add the web address and QR code.

www.copperhollowsproutworks.com

The QR Code for our web address has been uploaded

There is a lot of information and we are hoping it could be added to the label without a crowded look.

Thank you in advance for your designs.
Updates

It has been brought to our attention that we need to add a few things to the label.

Instead of NET WT. 2 OZ, it should read NET WT. 2 OZ (56.6 g)

At the bottom of the label, in addition to the web address, the following should be added. The content needs to be there, but it can be arranged differently to match the design. The • does not have to be there. Just looking to separate the two pieces of information.

Product of USA
Grown & Distributed by Copper Hollow Sproutworks
P.O. Box 614352 • Susanville, California 96127

```html
<!DOCTYPE html>
<html lang="en">
<head>
<meta charset="utf-8">
<title>Sunflower Microgreens Label</title>
<link href="https://fonts.googleapis.com/css2?family=Gochi+Hand&family=Montserrat:wght@400;600;700&display=swap" rel="stylesheet">
<style>
  :root {
    --orange-deep: #f26a22;
    --orange-mid: #f7a11c;
    --yellow: #fbd60c;
    --green: #2e6b30;
    --ink: #1f1f1f;
    --paper: #ffffff;
  }
  * { margin: 0; padding: 0; box-sizing: border-box; }
  html, body {
    width: 1198px;
    height: 1200px;
    overflow: hidden;
    background: var(--paper);
  }
  .label {
    position: relative;
    width: 1198px;
    height: 1200px;
    background: var(--paper);
    overflow: hidden;
    font-family: "Montserrat", Arial, sans-serif;
    color: var(--ink);
  }
  .label__waves {
    position: absolute;
    inset: 0;
    width: 100%;
    height: 100%;
  }
  .brand {
    position: absolute;
    left: 740px;
    top: 150px;
    width: 380px;
    display: flex;
    align-items: center;
    gap: 18px;
  }
  .brand__dot {
    flex: none;
    width: 54px;
    height: 54px;
    border-radius: 50%;
    background: var(--green);
  }
  .brand__name {
    font-weight: 700;
    font-size: 38px;
    line-height: 1.1;
    color: var(--green);
  }
  .product-name {
    font-family: "Gochi Hand", cursive;
    font-weight: 400;
    line-height: 1;
  }
  .product-name__line {
    position: absolute;
    left: 118px;
    white-space: nowrap;
    background: linear-gradient(90deg, var(--orange-deep), var(--yellow));
    -webkit-background-clip: text;
    background-clip: text;
    color: transparent;
  }
  .product-name__line--big {
    top: 118px;
    font-size: 220px;
    letter-spacing: 16px;
  }
  .product-name__line--mid {
    top: 318px;
    font-size: 132px;
    letter-spacing: 10px;
  }
  .product-name__line--green {
    top: 452px;
    font-size: 142px;
    letter-spacing: 0;
    color: var(--green);
    background: none;
    -webkit-text-stroke: 2px var(--green);
    text-shadow: 4px 4px 0 #fff, 6px 6px 0 rgba(46,107,48,0.35);
  }
  .tagline {
    position: absolute;
    left: 120px;
    top: 672px;
    font-size: 37px;
    line-height: 1.4;
    font-weight: 400;
  }
  .features {
    position: absolute;
    left: 248px;
    top: 900px;
    display: flex;
    gap: 74px;
    list-style: none;
  }
  .feature {
    width: 184px;
    height: 184px;
    border: 3px solid var(--ink);
    border-radius: 26px;
    display: flex;
    flex-direction: column;
    align-items: center;
    justify-content: center;
    gap: 12px;
    text-align: center;
    font-weight: 600;
    font-size: 24px;
    line-height: 1.2;
  }
  .feature--small { font-size: 19px; }
  .feature__icon { width: 46px; height: 46px; }
  .qr-code {
    position: absolute;
    left: 1008px;
    top: 930px;
    width: 120px;
    height: 120px;
    background: var(--paper);
    border: 3px solid var(--ink);
    border-radius: 8px;
  }
  .info {
    position: absolute;
    left: 0;
    right: 0;
    top: 1100px;
    text-align: center;
    line-height: 1.35;
  }
  .info__care {
    font-size: 20px;
    font-weight: 700;
  }
  .info__origin {
    font-size: 15px;
    font-weight: 600;
  }
  .info__web {
    font-size: 18px;
    font-weight: 700;
  }
</style>
</head>
<body>
<div class="label">
  <svg class="label__waves" viewBox="0 0 605 605" preserveAspectRatio="none" aria-hidden="true">
    <defs>
      <linearGradient id="sun-band" x1="0" y1="0" x2="1" y2="0">
        <stop offset="0" stop-color="#f26a22"/>
        <stop offset="0.55" stop-color="#f7a11c"/>
        <stop offset="1" stop-color="#fbd60c"/>
      </linearGradient>
    </defs>
    <path d="M0,466 C260,472 500,340 605,192 L605,232 C510,370 270,482 0,478 Z" fill="#2e6b30"/>
    <path d="M0,474 C275,484 520,370 605,226 L605,605 L0,605 Z" fill="url(#sun-band)"/>
  </svg>

  <div class="brand">
    <span class="brand__dot"></span>
    <span class="brand__name">Copper Hollow Sproutworks</span>
  </div>

  <h1 class="product-name">
    <span class="product-name__line product-name__line--big">SUN</span>
    <span class="product-name__line product-name__line--mid">FLOWER</span>
    <span class="product-name__line product-name__line--green">MICROGREENS</span>
  </h1>

  <p class="tagline">Naturally Grown Immune Boosting<br>Antioxidant Supperfood</p>

  <ul class="features">
    <li class="feature">
      <svg class="feature__icon" viewBox="0 0 24 24" fill="none" stroke="#1f1f1f" stroke-width="1.4">
        <path d="M12 22s7-7.5 7-13a7 7 0 0 0-14 0c0 5.5 7 13 7 13z"/>
        <circle cx="12" cy="9" r="2.6"/>
      </svg>
      <span>Locally<br>Grown</span>
    </li>
    <li class="feature">
      <svg class="feature__icon" viewBox="0 0 24 24">
        <circle cx="12" cy="12" r="10" fill="#1f1f1f"/>
      </svg>
      <span>Non<br>GMO</span>
    </li>
    <li class="feature feature--small">
      <svg class="feature__icon" viewBox="0 0 24 24" fill="none" stroke="#1f1f1f" stroke-width="1.4">
        <circle cx="12" cy="12" r="10.5"/>
        <path d="M12 19v-8"/>
        <path d="M12 11c0-3 2-5 5-5 0 3-2 5-5 5z"/>
        <path d="M12 13c0-2.5-1.8-4-4.5-4 0 2.5 1.8 4 4.5 4z"/>
      </svg>
      <span>Grown With<br>Organic Seeds</span>
    </li>
  </ul>

  <div class="qr-code" role="img" aria-label="QR code linking to www.copperhollowsproutworks.com"></div>

  <div class="info">
    <p class="info__care">NET WT. 2 OZ (56.6 g) &bull; Keep Refrigerated &bull; Thoroughly Wash Before Use</p>
    <p class="info__origin">Product of USA &bull; Grown &amp; Distributed by Copper Hollow Sproutworks &bull; P.O. Box 614352 &bull; Susanville, California 96127</p>
    <p class="info__web">www.copperhollowsproutworks.com</p>
  </div>
</div>
</body>
</html>
```